Young Balance Support Network

We need a poster explaining that some children live with a disability called Vestibular Disorder. Feel free to ask question. We want you to respect our color code, same as our logo.

Here is our website : http://www.ybsnetwork.org/

We need to sensibilise people about this disability for children.

Industry/Entity Type

Charity

Font styles to use
Serif

Requirements
Must have
• 1. our logo (with all our details) + one of the photo of Marek
• 2. design showing a child with a dizziness for exemple
• 3. a title saying : Aidez-nous à changer la vie des enfants vivant avec un problème vestibulaire
• 4.include the text attached (information flyer YBSN)
• Poster size : 24"X 36"
Should not have
• wheel chair

```html
<!DOCTYPE html>
<html lang="fr">
<head>
<meta charset="utf-8">
<title>Young Balance Support Network – Affiche</title>
<link href="https://fonts.googleapis.com/css2?family=Montserrat:wght@500;600;700;800&family=Open+Sans:wght@400;700&display=swap" rel="stylesheet">
<style>
  :root{
    --navy:#17435e;
    --sky:#3bb4e6;
    --panel:#9fdaf3;
    --ink:#1d3c50;
    --white:#ffffff;
    --green:#8cc63f;
  }
  *{margin:0;padding:0;box-sizing:border-box}
  html,body{width:800px;height:1200px;overflow:hidden;background:var(--white)}
  .poster{position:relative;width:800px;height:1200px;overflow:hidden;font-family:"Open Sans",sans-serif;color:var(--ink)}
  .masthead{position:absolute;left:0;top:0;width:800px;height:212px;background:var(--navy);text-align:center;padding-top:26px}
  .masthead .kicker{font-family:"Montserrat",sans-serif;font-weight:800;font-size:29px;letter-spacing:.5px;color:var(--sky);line-height:1}
  .masthead .headline{font-family:"Montserrat",sans-serif;font-weight:600;font-size:50px;line-height:57px;color:var(--white);margin-top:6px}
  .hero-photo{position:absolute;left:0;top:212px;width:800px;height:928px;
    background:linear-gradient(100deg,#f4f1ee 0%,#e9cdb8 30%,#d9ad8e 45%,#c79b72 58%,#f1efec 75%)}
  .info-panel{position:absolute;left:425px;top:212px;width:375px;height:928px;background:rgba(150,214,242,.93);padding:22px 32px 0 32px}
  .info-panel h2{font-family:"Montserrat",sans-serif;font-weight:700;font-size:27px;line-height:30px;color:var(--navy)}
  .info-panel p{font-size:12.3px;line-height:15px;text-align:justify;margin-top:0}
  .info-panel .intro{margin-top:18px}
  .info-panel .gap{margin-top:14px}
  .info-panel .second{margin-top:10px}
  .info-panel .aim{margin-top:14px}
  .logo-card{position:absolute;left:458px;top:938px;width:297px;height:166px;background:var(--white);border-radius:3px;padding:22px 18px;display:flex;align-items:center;gap:16px}
  .logo-card .name{font-family:"Montserrat",sans-serif;font-weight:800;font-size:17px;line-height:20px;color:var(--navy);letter-spacing:.5px}
  .logo-card .handle{font-family:"Montserrat",sans-serif;font-weight:800;font-size:13px;color:var(--navy);margin-top:14px}
  .logo-card .dot{flex:none;width:78px;height:78px;border-radius:50%;background:var(--sky)}
  .contact-bar{position:absolute;left:0;top:1140px;width:800px;height:60px;background:var(--navy);color:var(--white);
    font-family:"Montserrat",sans-serif;font-weight:600;font-size:19px;display:flex;align-items:center;justify-content:center;gap:6px}
  .contact-bar svg{width:18px;height:18px}
</style>
</head>
<body>
<div class="poster">
  <header class="masthead">
    <div class="kicker">AIDEZ-NOUS À CHANGER LA VIE DES</div>
    <h1 class="headline">enfants vivant avec un<br>problème vestibulaire</h1>
  </header>

  <div class="hero-photo" role="img" aria-label="Photo d'une fillette aux tresses blondes, la main sur le front, les yeux plissés, prise de vertige"></div>

  <section class="info-panel">
    <h2>Qu’est-ce que<br>le vestibule ?</h2>
    <p class="intro">C’est un organe sensoriel, pilier de votre équilibre, véritable 6ème sens situé dans l’oreille interne.<br>
    Qu’est ce qu’une aréflexie vestibulaire ?<br>
    C’est l’absence complète de toute information vestibulaire. L’enfant a ainsi l’impression que tout vacille autour de lui, jour et nuit.<br>
    Quelles en sont les conséquences pour l’enfant ?<br>
    Le développement moteur de l’enfant est retardé car il doit trouver des solutions afin de construire son équilibre, stabiliser son regard et son corps.</p>
    <p class="gap">Certains apprentissages sont de véritables obstacles pour l’enfant : se représenter son propre corps, se situer dans l’espace qui l’entoure, interagir avec les autres, communiquer, écrire, lire, manger, boire, marcher. Chacune de ces actions nécessitent des efforts considérables pour se concentrer quelques secondes ou minutes.</p>
    <p class="gap">Quand l’enfant réussit à effectuer l’une de ces actions, son comportement peut sembler déroutant et bien trop souvent mal interprété par le grand public.</p>
    <h2 class="second">Quel est le but de<br>notre association ?</h2>
    <p class="aim">Notre association a pour but de promouvoir les troubles vestibulaires chez l’enfant, ses conséquences sur sa santé ainsi que celui de son entourage et de soutenir ces enfants et leurs parents en leur offrant un espace de parole et des solutions concrètes pour soulager leur quotidien. Notre association a également pour but de financer et promouvoir toute action de recherche scientifique visant à aider les enfants ayant un trouble vestibulaire.</p>
  </section>

  <div class="logo-card">
    <div>
      <div class="name">YOUNG<br>BALANCE<br>SUPPORT<br>NETWORK</div>
      <div class="handle">@ybsnetwork</div>
    </div>
    <span class="dot"></span>
  </div>

  <footer class="contact-bar">
    <svg viewBox="0 0 24 24" fill="none" stroke="#fff" stroke-width="2"><path d="M5 3h4l2 5-2.5 1.5a11 11 0 0 0 6 6L16 13l5 2v4a2 2 0 0 1-2 2A16 16 0 0 1 3 5a2 2 0 0 1 2-2z"/></svg>
    <span>14-555012-7 | www.ybsnetwork.org | info@ybsnetwork.org</span>
  </footer>
</div>
</body>
</html>
```